Advertisement for linkora Ad

We are looking to copy a mailer style design that would normally be sent out to a mailbox. However we have decided to simply use it and run an add on Linkora. please check photo sizes for linkora to make sure your design will work.

also please try to use the colors from our website: brightmeadowclub@postvane.net

we want the same layout as the ad we sent in the files, with different photos and color scheme.

Target Market(s)

dog owners with busy schedules

Font styles to use
Sans Serif

Colors

Designer to choose only greyscale colors for use in the design.

```html
<!DOCTYPE html>
<html lang="en">
<head>
<meta charset="utf-8">
<title>Bright Meadow Canine Club – Dog Daycare Ad</title>
<link rel="stylesheet" href="https://fonts.googleapis.com/css2?family=Oswald:wght@500;600&family=Arimo:wght@400&display=swap">
<style>
  :root {
    --panel: #4a4a4a;
    --panel-dark: #3c3c3c;
    --band-top: #3a3a3a;
    --band-bottom: #262626;
    --headline: #ededed;
    --offer-title: #d4d4d4;
    --white: #ffffff;
    --dots: #bdbdbd;
    --photo-light: #dcdcdc;
    --photo-mid: #c4c4c4;
    --photo-dark: #a9a9a9;
    --photo-glow: #f4f4f4;
    --logo-ink: #111111;
  }
  * { margin: 0; padding: 0; box-sizing: border-box; }
  html, body { width: 1200px; height: 457px; overflow: hidden; background: var(--panel); }
  .ad {
    position: relative;
    width: 1200px;
    height: 457px;
    overflow: hidden;
    font-family: "Arimo", Arial, sans-serif;
  }
  .hero {
    position: absolute;
    inset: 0 0 auto 0;
    height: 301px;
    background: linear-gradient(90deg, var(--panel-dark) 0%, var(--panel) 60%, #454545 100%);
  }
  .hero-photo {
    position: absolute;
    left: 0; top: 0;
    width: 673px; height: 301px;
    clip-path: polygon(0 0, 571px 0, 673px 301px, 0 301px);
    background:
      radial-gradient(ellipse at 55% 45%, var(--photo-glow) 0%, rgba(244,244,244,0.7) 28%, rgba(244,244,244,0) 55%),
      linear-gradient(100deg, var(--photo-light) 0%, var(--photo-mid) 55%, var(--photo-dark) 100%);
  }
  .brand {
    position: absolute;
    left: 18px; top: 262px;
    display: flex; align-items: center; gap: 8px;
    font-family: "Oswald", Arial, sans-serif;
    font-weight: 600;
    font-size: 17px;
    letter-spacing: 0.5px;
    text-transform: uppercase;
    color: var(--logo-ink);
  }
  .brand-mark { width: 12px; height: 12px; background: var(--logo-ink); }
  .hero-copy {
    position: absolute;
    left: 741px; top: 14px;
    color: var(--white);
  }
  .headline {
    font-family: "Oswald", Arial, sans-serif;
    font-weight: 600;
    font-size: 38px;
    line-height: 40px;
    letter-spacing: 3.6px;
    color: var(--headline);
    text-transform: uppercase;
  }
  .perks { list-style: none; margin-top: -2px; }
  .perks li { font-size: 18px; line-height: 26px; }
  .perks .friend { margin-top: 16px; }
  .contact { margin-top: 0; font-size: 14px; line-height: 17.5px; letter-spacing: 1px; font-style: normal; }
  .offers {
    position: absolute;
    left: 0; top: 301px;
    width: 1200px; height: 156px;
    background: linear-gradient(160deg, var(--band-top) 0%, #303030 55%, var(--band-bottom) 100%);
    display: grid;
    grid-template-columns: 417px 426px 357px;
  }
  .offer {
    position: relative;
    text-align: center;
    padding-top: 26px;
  }
  .offer + .offer::before {
    content: "";
    position: absolute;
    left: 0; top: 15px; bottom: 12px;
    border-left: 3px dotted var(--dots);
  }
  .offer-title {
    font-family: "Oswald", Arial, sans-serif;
    font-weight: 600;
    font-size: 26px;
    line-height: 26px;
    letter-spacing: 2px;
    color: var(--offer-title);
    text-transform: uppercase;
  }
  .offer-expiry {
    margin-top: 2px;
    font-family: "Oswald", Arial, sans-serif;
    font-weight: 500;
    font-size: 16px;
    letter-spacing: 1px;
    color: var(--white);
  }
  .offer--daycare { padding-right: 52px; }
  .offer--bath { padding-right: 20px; }
</style>
</head>
<body>
<main class="ad">
  <section class="hero">
    <div class="hero-photo" role="img" aria-label="Photo of a litter of white puppies sleeping in a circle on a light wood floor"></div>
    <div class="brand"><span class="brand-mark"></span>Bright Meadow Canine Club</div>
    <div class="hero-copy">
      <h1 class="headline">Not your typical<br>dog daycare</h1>
      <ul class="perks">
        <li>SAFE, OPEN-PLAY DAYCARE</li>
        <li>EXCERCISE &amp; EDUCATION</li>
        <li>FUN FILLED DAYS WITH</li>
        <li>THEIR BEEF</li>
        <li class="friend">(BEST FURRY FRIEND FOREVER)</li>
      </ul>
      <address class="contact">
        Bright Meadow Canine Club<br>
        418 North Elm Avenue Maple Grove IA<br>
        555-204-7731
      </address>
    </div>
  </section>
  <section class="offers">
    <div class="offer offer--daycare">
      <p class="offer-title">Free first day<br>of daycare!*</p>
      <p class="offer-expiry">use by 8/31/20</p>
    </div>
    <div class="offer offer--bath">
      <p class="offer-title">One free<br>bath!*</p>
      <p class="offer-expiry">use by 8/31/20</p>
    </div>
    <div class="offer offer--groom">
      <p class="offer-title">$20 off<br>first groom</p>
      <p class="offer-expiry">use by 8/31/20</p>
    </div>
  </section>
</main>
</body>
</html>
```